Custom Framing Shop Stonebrook Framing Studio

I want an eye catching graphic that will be used a s business sign on a busy road. The sign MUST communicate the type of business it is clearly to vehicles traveling at 40 mph. This is a custom picture framing business and the sign will be hanging and be approximately 32" X 48". The business name is Stonebrook Framing Studio; Custom framing: by appointment and should include a whole or partial image of a picture frame as a visual que. I've included inspiration idea's, color pallets and styles that I like and a current business card for inspiration. I like the crimson font style shadowing and background colors of the attached Pello's pizzeria sign. I'd prefer crimson letters. Custom Framing is the message to communicate, followed by phone number and business name. I like the idea of a shield shape with a banner since it would more eye catching, Once again the Stonebrook image and name is less important than communicating what the business does. I like Crimson, grey, gold, black but am open to new ideas . I like the idea of a shield with a banner more than a rectangle, but am open to idea's

Target Market(s)

My target market is local homeowners ($700k+) who want a relationship with their framer and are willing to pay for a customized experience compared to a craft store experience. I have more female clients then men.

Industry/Entity Type

Picture Framing Art

Other font styles liked:
• Look at the attached image of a custom pizzeria sign, its kid of a custom car pinstripe font style. Script and decorative may be difficult to read while driving by but add to the elegance.

Colors

Designer to choose colors to be used in the design.

Requirements
Must have
• Clearly communicate what the business does "Custom framing" preferably with a picture frame and words
Nice to have
• incorporate a Stonebrook into the graphic
Should not have
• A Stonebrook image doesn't communicate what the business does to a vehicle traveling at 40 mph by the sign

```html
<!DOCTYPE html>
<html lang="en">
<head>
<meta charset="utf-8">
<title>Stonebrook Framing Studio – Hanging Sign</title>
<link rel="stylesheet" href="https://fonts.googleapis.com/css2?family=Lobster+Two:wght@700&family=Montserrat:wght@600;700;800&display=swap">
<style>
  :root {
    --crimson: #761418;
    --crimson-deep: #5c0f12;
    --gold-light: #f3dd8a;
    --gold: #d6b25a;
    --gold-dark: #a9822f;
    --frame-light: #efe2bd;
    --frame-dark: #cdb681;
    --cream-top: #fbf4dc;
    --cream: #f5ead3;
    --ink: #111111;
    --white: #ffffff;
    --page: #ffffff;
  }
  html, body {
    margin: 0;
    padding: 0;
    width: 882px;
    height: 1200px;
    overflow: hidden;
    background: var(--page);
  }
  .canvas {
    position: relative;
    width: 882px;
    height: 1200px;
  }
  .shop-sign {
    position: absolute;
    left: 21px;
    top: 322px;
    width: 840px;
    height: 556px;
    filter: drop-shadow(0 6px 10px rgba(0,0,0,0.18));
  }
  .sign-headline {
    font-family: "Lobster Two", cursive;
    font-weight: 700;
    fill: var(--white);
  }
  .sign-phone {
    font-family: "Montserrat", sans-serif;
    font-weight: 700;
    fill: var(--ink);
  }
  .brand-name {
    font-family: "Montserrat", sans-serif;
    font-weight: 800;
    fill: var(--ink);
  }
  .brand-tagline {
    font-family: "Montserrat", sans-serif;
    font-weight: 600;
    fill: var(--ink);
  }
  .brand-mark { fill: var(--crimson); }
  .ornament { fill: var(--crimson); opacity: 0.35; }
</style>
</head>
<body>
<main class="canvas">
  <svg class="shop-sign" viewBox="0 0 1210 800" xmlns="http://www.w3.org/2000/svg" aria-label="Stonebrook Framing Studio hanging sign: Custom framing">
    <defs>
      <path id="sign-outline" d="M330 0 H880 Q930 0 950 40 L960 65 H1140 V110 H1165 V200 Q1210 300 1210 400 Q1210 500 1165 600 V690 H1140 V735 H960 L950 760 Q930 800 880 800 H330 Q280 800 260 760 L250 735 H70 V690 H45 V600 Q0 500 0 400 Q0 300 45 200 V110 H70 V65 H250 L260 40 Q280 0 330 0 Z"/>
      <linearGradient id="gold-edge" x1="0" y1="0" x2="1" y2="1">
        <stop offset="0" stop-color="var(--gold-light)"/>
        <stop offset="0.5" stop-color="var(--gold)"/>
        <stop offset="1" stop-color="var(--gold-dark)"/>
      </linearGradient>
      <linearGradient id="cream-panel" x1="0" y1="0" x2="0" y2="1">
        <stop offset="0" stop-color="var(--cream-top)"/>
        <stop offset="1" stop-color="var(--cream)"/>
      </linearGradient>
      <linearGradient id="frame-moulding" x1="0" y1="0" x2="1" y2="1">
        <stop offset="0" stop-color="var(--frame-light)"/>
        <stop offset="1" stop-color="var(--frame-dark)"/>
      </linearGradient>
      <clipPath id="panel-clip">
        <use href="#sign-outline" transform="translate(605 400) scale(0.935 0.905) translate(-605 -400)"/>
      </clipPath>
    </defs>

    <!-- sign body layers -->
    <use class="sign-edge" href="#sign-outline" fill="url(#gold-edge)"/>
    <use class="sign-border" href="#sign-outline" fill="var(--crimson)" transform="translate(605 400) scale(0.985 0.978) translate(-605 -400)"/>
    <use class="sign-inner-line" href="#sign-outline" fill="url(#gold-edge)" transform="translate(605 400) scale(0.945 0.92) translate(-605 -400)"/>
    <use class="sign-panel" href="#sign-outline" fill="url(#cream-panel)" transform="translate(605 400) scale(0.935 0.905) translate(-605 -400)"/>

    <!-- crimson banner -->
    <g class="banner" clip-path="url(#panel-clip)">
      <rect x="0" y="275" width="1210" height="250" fill="var(--crimson)"/>
    </g>

    <!-- picture frame -->
    <g class="picture-frame">
      <path fill-rule="evenodd" fill="url(#frame-moulding)" d="M275 235 H935 V565 H275 Z M315 275 V525 H895 V275 Z"/>
      <rect x="275" y="235" width="660" height="330" fill="none" stroke="var(--gold-dark)" stroke-width="2"/>
      <rect x="315" y="275" width="580" height="250" fill="var(--crimson)" stroke="var(--gold-dark)" stroke-width="2"/>
    </g>

    <!-- brand -->
    <g class="brand">
      <rect class="brand-mark" x="430" y="125" width="36" height="36"/>
      <text class="brand-name" x="478" y="160" font-size="46">Stonebrook</text>
      <text class="brand-tagline" x="775" y="196" font-size="22" text-anchor="end">Framing Studio</text>
    </g>

    <!-- headline -->
    <text class="sign-headline" x="605" y="445" font-size="170" text-anchor="middle" textLength="1015" lengthAdjust="spacingAndGlyphs">Custom framing</text>

    <!-- phone -->
    <text class="sign-phone" x="605" y="662" font-size="100" text-anchor="middle" textLength="765" lengthAdjust="spacingAndGlyphs">(555) 014-2970</text>

    <!-- ornament area -->
    <rect class="ornament" role="img" aria-label="Decorative scroll flourish" x="470" y="690" width="270" height="42" rx="21"/>
  </svg>
</main>
</body>
</html>
```